Tarnobe presentation

We built A 20-page powerpoint document. We would like to change the look of this document. We work in digital area. So, we would like something more modern, more current and less classical. We need to be fashionable while remaining reassuring for corporate. Our business is to make recommendations in 5 days where our competitors do it in 3 months.

Target Market(s)

medium sized business, or a large global enterprise

Industry/Entity Type

Digital

Colors

Designer to choose colors to be used in the design.

Requirements
Must have
• We are working with digital expert. We need to surprise them.

```html
<!DOCTYPE html>
<html lang="fr">
<head>
<meta charset="utf-8">
<title>Tarnobe — 360° Digital Sprint Assessment</title>
<link href="https://fonts.googleapis.com/css2?family=Bebas+Neue&family=Montserrat:wght@400;600;700&display=swap" rel="stylesheet">
<style>
:root{
  --navy-1:#26335e;
  --navy-2:#151b34;
  --white:#ffffff;
  --cyan:#5ff3f0;
  --blue:#2f7cf6;
  --red:#f0324b;
  --orange:#f7a21b;
  --green:#9fd62c;
  --pink:#e8247c;
  --purple:#7b2fb0;
  --lime:#b5f08f;
  --yellow:#f6d52c;
  --muted:#b9c2dd;
  --page-num:#1f86c8;
}
*{box-sizing:border-box;margin:0;padding:0}
html,body{width:1200px;height:1200px;overflow:hidden;background:#fff}
body{position:relative;font-family:"Montserrat",Arial,sans-serif;color:var(--white)}
.page-number{position:absolute;top:10px;right:20px;font-family:"Montserrat",sans-serif;font-weight:700;font-size:17px;color:var(--page-num)}
.deck{position:absolute;top:103px;left:30px;display:grid;grid-template-columns:repeat(4,278px);grid-auto-rows:156px;column-gap:11px;row-gap:14px}
.slide{position:relative;overflow:hidden;background:linear-gradient(160deg,var(--navy-1),var(--navy-2))}
.display{font-family:"Bebas Neue",Impact,sans-serif;line-height:.95;letter-spacing:.3px}
.kicker{position:absolute;left:14px;top:13px;font-family:"Bebas Neue",sans-serif;font-size:9px;color:var(--white)}
.title{position:absolute;left:14px;top:28px;font-size:22px}
.brand{position:absolute;right:10px;bottom:8px;display:flex;align-items:center;gap:3px;font-weight:700;font-size:7px;color:var(--white)}
.brand::before{content:"";width:7px;height:7px;border-radius:50%;background:var(--blue)}
.figure-runner{position:absolute;border-radius:40% 40% 30% 30%;background:linear-gradient(170deg,var(--orange),var(--pink) 45%,var(--blue) 80%,var(--cyan));opacity:.9}
.body-text{font-size:5.5px;line-height:1.45;color:var(--muted)}
.big-num{position:absolute;font-family:"Bebas Neue",sans-serif;font-size:190px;line-height:1;top:-10px}
.section-title{position:absolute;left:120px;font-size:32px}
/* experts */
.expert{position:absolute;top:62px;width:122px}
.expert .photo{position:absolute;left:0;top:0;width:38px;height:38px;border-radius:50%;border:2px solid var(--yellow);background:linear-gradient(160deg,#d8d8d8,#6d6d6d)}
.expert .info{position:absolute;left:46px;top:0;width:78px}
.expert .name{font-size:5px;font-weight:700;color:var(--blue)}
.expert .tags{font-size:4px;color:var(--muted);margin-bottom:4px}
.expert p{font-size:4px;line-height:1.35;color:var(--muted);margin-bottom:3px}
.expert u{color:var(--white)}
/* references */
.refs{position:absolute;left:14px;top:60px;width:252px;border-collapse:collapse}
.refs td{font-size:4.2px;line-height:1.3;padding:0 0 4px;vertical-align:top;color:var(--white)}
.refs td.client{width:58px;font-weight:700;color:var(--yellow)}
.quote{position:absolute;left:28px;top:50px;font-size:24px}
</style>
</head>
<body>
<div class="page-number">24</div>

<main class="deck">

  <!-- 1 cover -->
  <section class="slide">
    <div class="brand" style="left:26px;top:12px;right:auto;bottom:auto;font-size:9px">Tarnobe</div>
    <div class="display" style="position:absolute;left:24px;top:62px;font-size:28px">360° DIGITAL</div>
    <div class="display" style="position:absolute;left:24px;top:90px;font-size:28px;color:var(--cyan)">SPRINT ASSESSMENT</div>
    <div class="display" style="position:absolute;left:26px;top:128px;font-size:12px">13 JUILLET 2017</div>
    <div class="figure-runner" role="img" aria-label="Coureur stylisé en facettes colorées" style="left:198px;top:14px;width:56px;height:130px"></div>
  </section>

  <!-- 2 quote -->
  <section class="slide">
    <div class="display quote" style="left:28px;top:50px;font-size:25px">« LE DÉNI DE VOIR<br>L'ÉVOLUTION EST UN DÉLIT! »</div>
    <div class="brand">Tarnobe</div>
  </section>

  <!-- 3 sommaire -->
  <section class="slide">
    <div class="display" style="position:absolute;left:72px;top:20px;font-size:26px">SOMMAIRE</div>
    <div class="display" style="position:absolute;left:0;top:50px;width:166px;height:8px;background:var(--blue);font-size:7px;padding:1px 0 0 74px">1/ LE SPRINT C'EST QUOI ?</div>
    <div style="position:absolute;left:74px;top:60px;font-size:3.5px;line-height:1.4;color:var(--muted)">A/ Un concept innovant<br>B/ Partis-pris interconnectés<br>C/ Livrables<br>D/ Experts</div>
    <div class="display" style="position:absolute;left:0;top:82px;width:166px;height:8px;background:var(--red);font-size:7px;padding:1px 0 0 74px">2/ PROCESS DÉTAILLÉ</div>
    <div style="position:absolute;left:74px;top:92px;font-size:3.5px;line-height:1.4;color:var(--muted)">Questionnement préalable<br>Jour 1 : enrichissement du questionnement<br>Jour 2 : la vision 360°<br>Jour 3 : les leviers de la transformation<br>Jour 4 : transformer la façon de se transformer<br>Jour 5 : on se lance !<br>Le jour d'après</div>
    <div class="display" style="position:absolute;left:0;top:132px;width:166px;height:8px;background:var(--green);font-size:7px;padding:1px 0 0 74px">3/ RÉFÉRENCES DES EXPERTS</div>
    <div class="figure-runner" role="img" aria-label="Coureur stylisé en facettes colorées" style="left:186px;top:28px;width:36px;height:92px"></div>
    <div class="brand">Tarnobe</div>
  </section>

  <!-- 4 section 1 -->
  <section class="slide">
    <div class="big-num" style="left:40px;color:var(--cyan)">1</div>
    <div class="display section-title" style="top:62px">LE SPRINT<br>C'EST QUOI ?</div>
    <div class="brand">Tarnobe</div>
  </section>

  <!-- 5 concept -->
  <section class="slide">
    <div class="kicker">1 LE SPRINT C'EST QUOI ?</div>
    <div class="display title" style="top:36px;font-size:22px">A/ UN CONCEPT<br>INNOVANT:</div>
    <svg width="278" height="156" style="position:absolute;left:0;top:0" font-family="Montserrat" font-size="3.6" font-weight="700" fill="#fff" text-anchor="middle">
      <g>
        <polygon points="138,94 148,88 158,94 158,106 148,112 138,106" fill="var(--blue)"/><text x="148" y="100" >Conjugaison de</text><text x="148" y="105">high expertise</text>
        <polygon points="160,82 170,76 180,82 180,94 170,100 160,94" fill="var(--orange)"/><text x="170" y="87">Avec</text><text x="170" y="92">efficacité</text>
        <polygon points="182,94 192,88 202,94 202,106 192,112 182,106" fill="var(--green)"/><text x="192" y="99">Regarder</text><text x="192" y="104">autrement</text>
        <polygon points="160,106 170,100 180,106 180,118 170,124 160,118" fill="var(--red)"/><text x="170" y="111">Imaginer</text><text x="170" y="116">librement</text>
        <polygon points="205,82 215,76 225,82 225,94 215,100 205,94" fill="var(--pink)"/><text x="215" y="87">5 heures</text><text x="215" y="92">chrono</text>
        <polygon points="205,106 215,100 225,106 225,118 215,124 205,118" fill="var(--pink)"/><text x="215" y="111">Proposer avec</text><text x="215" y="116">générosité</text>
      </g>
    </svg>
    <div class="brand">Tarnobe</div>
  </section>

  <!-- 6 partis-pris -->
  <section class="slide">
    <div class="kicker">1 LE SPRINT C'EST QUOI ?</div>
    <div class="display title" style="top:32px;font-size:19px">B/ PARTIS-PRIS: UNE APPROCHE D'<br>EXPERTISES INTERCONNECTÉES</div>
    <svg width="278" height="156" style="position:absolute;left:0;top:0" font-family="Montserrat" font-size="3.3" font-weight="700" fill="#fff" text-anchor="middle">
      <circle cx="44" cy="104" r="31" fill="var(--blue)"/>
      <circle cx="100" cy="104" r="31" fill="var(--green)" opacity=".95"/>
      <circle cx="156" cy="104" r="31" fill="var(--pink)" opacity=".95"/>
      <text x="42" y="97">Une vision</text><text x="42" y="102">pluridisciplinaire :</text><text x="42" y="107">SI, data, communication,</text><text x="42" y="112">excellence opérationnelle</text>
      <text x="100" y="100">Un état d'esprit</text><text x="100" y="105">et des outils</text><text x="100" y="110">design thinking</text>
      <text x="160" y="97">Une volonté farouche</text><text x="160" y="102">de présenter des</text><text x="160" y="107">solutions audacieuses,</text><text x="160" y="112">réalistes et opérationnelles</text>
    </svg>
    <div class="brand">Tarnobe</div>
  </section>

  <!-- 7 livrables -->
  <section class="slide">
    <div class="kicker">1 LE SPRINT C'EST QUOI ?</div>
    <div class="display title" style="font-size:22px">C/ LIVRABLES</div>
    <div class="body-text" style="position:absolute;left:14px;top:58px;width:98px;font-size:4.6px">
      <p style="margin-bottom:6px">1/ Un état des lieux</p>
      <p style="margin-bottom:6px">2/ Mise en perspective de vos challenges digitaux stimulés par l'approche Design Thinking</p>
      <p>3/ La mise en avant des points-clés sur lesquels se déterminer pour faire évoluer votre stratégie digitale en termes de :</p>
    </div>
    <ul class="display" style="position:absolute;left:146px;top:62px;list-style:none;font-size:7.5px;line-height:1">
      <li style="margin-bottom:6px"><span style="display:inline-block;width:6px;height:6px;border-radius:50%;background:var(--blue);margin-right:6px"></span>Excellence Opérationnelle</li>
      <li style="margin-bottom:6px"><span style="display:inline-block;width:6px;height:6px;background:var(--white);margin-right:6px"></span>Organisation du Système d'information</li>
      <li style="margin-bottom:6px"><span style="display:inline-block;width:6px;height:6px;background:var(--orange);margin-right:6px"></span>Stratégie Data</li>
      <li style="margin-bottom:6px"><span style="display:inline-block;width:6px;height:6px;border-radius:50%;background:var(--pink);margin-right:6px"></span>Communication Digitale</li>
      <li><span style="display:inline-block;width:6px;height:6px;border-radius:50%;background:var(--purple);margin-right:6px"></span>Intelligence Collective</li>
    </ul>
    <div class="brand">Tarnobe</div>
  </section>

  <!-- 8 experts -->
  <section class="slide">
    <div class="kicker">1 LE SPRINT C'EST QUOI ?</div>
    <div class="display title" style="font-size:22px">D/ EXPERTS</div>
    <div class="expert" style="left:12px">
      <div class="photo" role="img" aria-label="Portrait de Claire Venot"></div>
      <div class="info"><div class="name">Claire Venot</div><div class="tags">#Communication #Innovation</div>
        <p><u>Domaines de compétences</u> : communication, marque, innovation, transformation digitale.</p>
        <p><u>Challenge</u> : accompagner la transformation des entreprises par le levier humain.</p>
        <p><u>Motto</u> : l'adaptabilité s'acquiert par l'expérience.</p></div>
    </div>
    <div class="expert" style="left:144px">
      <div class="photo" role="img" aria-label="Portrait de Marc Elbaz"></div>
      <div class="info"><div class="name">Marc Elbaz</div><div class="tags">#Communication #Formation</div>
        <p><u>Domaines de compétences</u> : communication et marque, accompagnement du changement.</p>
        <p><u>Challenge</u> : considérer la marque comme un dispositif innovant.</p>
        <p><u>Motto</u> : la vraie valeur d'un produit se révèle à l'usage.</p></div>
    </div>
    <div class="brand">Tarnobe</div>
  </section>

  <!-- 9 experts -->
  <section class="slide">
    <div class="kicker">1 LE SPRINT C'EST QUOI ?</div>
    <div class="display title" style="font-size:22px">D/ EXPERTS</div>
    <div class="expert" style="left:12px">
      <div class="photo" role="img" aria-label="Portrait de Luc Ferrand"></div>
      <div class="info"><div class="name">Luc Ferrand</div><div class="tags">#Stratégie #Transformation</div>
        <p><u>Domaines de compétences</u> : entrepreneuriat, management, lean, accompagnement du changement.</p>
        <p><u>Challenge</u> : atteindre ensemble le sommet.</p>
        <p><u>Motto</u> : si vous voulez aller vite, allez-y seul.</p></div>
    </div>
    <div class="expert" style="left:144px">
      <div class="photo" role="img" aria-label="Portrait d'Inès Morvan"></div>
      <div class="info"><div class="name">Inès Morvan</div><div class="tags">#DesignThinking #Collectif</div>
        <p><u>Domaines de compétences</u> : design, architecture, entrepreneuriat, recherche.</p>
        <p><u>Challenge</u> : réconcilier les enjeux avec les besoins de l'usager.</p>
        <p><u>Motto</u> : il faut toujours viser la lune.</p></div>
    </div>
    <div class="brand">Tarnobe</div>
  </section>

  <!-- 10 experts -->
  <section class="slide">
    <div class="kicker">1 LE SPRINT C'EST QUOI ?</div>
    <div class="display title" style="font-size:22px">D/ EXPERTS</div>
    <div class="expert" style="left:12px">
      <div class="photo" role="img" aria-label="Portrait de Paul Garnier"></div>
      <div class="info"><div class="name">Paul Garnier</div><div class="tags">#DataStrategy #MachineLearning</div>
        <p><u>Domaines de compétences</u> : marketing et relation client, machine learning, coaching.</p>
        <p><u>Challenge</u> : vous guider vers votre vraie question.</p>
        <p><u>Motto</u> : exploiter la donnée est un projet métier.</p></div>
    </div>
    <div class="expert" style="left:144px">
      <div class="photo" role="img" aria-label="Portrait d'Hugo Lemaire"></div>
      <div class="info"><div class="name">Hugo Lemaire</div><div class="tags">#BigData #Python</div>
        <p><u>Domaines de compétences</u> : entrepreneuriat, coaching d'organisations, infrastructure.</p>
        <p><u>Challenge</u> : vous rendre autonome sur vos données.</p>
        <p><u>Motto</u> : les data nous font passer de l'ère de l'alignement.</p></div>
    </div>
    <div class="brand">Tarnobe</div>
  </section>

  <!-- 11 expert -->
  <section class="slide">
    <div class="kicker">1 LE SPRINT C'EST QUOI ?</div>
    <div class="display title" style="font-size:22px">D/ EXPERTS</div>
    <div class="expert" style="left:12px">
      <div class="photo" role="img" aria-label="Portrait de Karim Belhadj"></div>
      <div class="info"><div class="name">Karim Belhadj</div><div class="tags">#Architecte #Cloud</div>
        <p><u>Domaines de compétences</u> : architecture SI, nouvelles technologies, accompagnement.</p>
        <p><u>Challenge</u> : vous apprendre à développer vos nouvelles idées.</p>
        <p><u>Motto</u> : le véritable voyage de découverte consiste à regarder autrement.</p></div>
    </div>
    <div class="brand">Tarnobe</div>
  </section>

  <!-- 12 section 2 -->
  <section class="slide">
    <div class="big-num" style="left:50px;color:var(--lime)">2</div>
    <div class="display section-title" style="top:62px">PROCESS<br>DÉTAILLÉ</div>
    <div class="brand">Tarnobe</div>
  </section>

  <!-- 13 préparation -->
  <section class="slide">
    <div class="kicker" style="color:var(--green)">2/ PROCESS DÉTAILLÉ</div>
    <div class="display title" style="top:32px;font-size:19px">PRÉPARATION DU SPRINT:<br>QUESTIONNEMENT CLIENT</div>
    <div class="display" style="position:absolute;left:14px;top:80px;font-size:46px;color:var(--green)">?</div>
    <div style="position:absolute;left:44px;top:86px;font-size:7px;font-weight:600;line-height:1.25">Questionnement<br>préalable au sprint</div>
    <div style="position:absolute;left:44px;top:106px;font-size:5px;font-weight:600;color:var(--blue);line-height:1.3">Envoi Questionnaire client<br>par Tarnobe</div>
    <svg width="40" height="40" style="position:absolute;left:146px;top:80px" viewBox="0 0 40 40" role="img" aria-label="Icône cible">
      <circle cx="20" cy="20" r="16" fill="none" stroke="var(--pink)" stroke-width="4"/>
      <circle cx="20" cy="20" r="8" fill="none" stroke="var(--pink)" stroke-width="4"/>
      <path d="M20 20 L36 4" stroke="var(--white)" stroke-width="2"/>
    </svg>
    <div style="position:absolute;left:190px;top:90px;font-size:7px;font-weight:600;line-height:1.3">Identification of<br>needs &amp; objectives</div>
    <div class="brand">Tarnobe</div>
  </section>

  <!-- 14 jour 1 -->
  <section class="slide">
    <div class="kicker" style="color:var(--green)">2/ PROCESS DÉTAILLÉ</div>
    <div class="display title" style="top:32px;font-size:19px">JOUR 1 : VERS UN<br>ENRICHISSEMENT DU<br>QUESTIONNEMENT</div>
    <svg width="100" height="100" viewBox="-50 -50 100 100" style="position:absolute;left:170px;top:38px" font-family="Montserrat" font-size="3.6" font-weight="700" fill="#fff" text-anchor="middle">
      <path d="M0 0 L0 -48 A48 48 0 0 1 41.6 24 Z" fill="var(--green)"/>
      <path d="M0 0 L41.6 24 A48 48 0 0 1 -41.6 24 Z" fill="var(--blue)"/>
      <path d="M0 0 L-41.6 24 A48 48 0 0 1 0 -48 Z" fill="var(--pink)"/>
      <circle r="14" fill="var(--navy-2)"/>
      <text y="-1" font-family="Bebas Neue" font-size="6">DESIGN</text><text y="5" font-family="Bebas Neue" font-size="6">THINKING</text>
      <text x="23" y="-14">Questionnement</text><text x="23" y="-10">client et point</text><text x="23" y="-6">de vue augmenté</text>
      <text x="-25" y="-6">Clarification</text><text x="-25" y="-2">des enjeux</text><text x="-25" y="2">par digital</text>
      <text y="30">Besoins et objectifs</text><text y="35">du client</text>
    </svg>
    <div class="brand">Tarnobe</div>
  </section>

  <!-- 15 jour 2 -->
  <section class="slide">
    <div class="kicker" style="color:var(--green)">2/ PROCESS DÉTAILLÉ</div>
    <div class="display title" style="top:34px;font-size:19px">JOUR 2 : LA VISION 360°</div>
    <div style="position:absolute;left:14px;top:66px;display:flex;gap:5px">
      <div style="width:46px;height:74px;background:var(--blue);padding:3px;font-size:3.5px;line-height:1.35"><div class="display" style="font-size:5.5px;margin-bottom:3px">ÉTAT D'ESPRIT COLLABORATIF</div>Compréhension du challenge. Identification des parties prenantes. Articulation des insights.</div>
      <div style="width:46px;height:74px;background:var(--red);padding:3px;font-size:3.5px;line-height:1.35"><div class="display" style="font-size:5.5px;margin-bottom:3px">STRATÉGIE DATA</div>Information des données. Objectifs de développement. Plan d'actions.</div>
      <div style="width:46px;height:74px;background:var(--orange);padding:3px;font-size:3.5px;line-height:1.35"><div class="display" style="font-size:5.5px;margin-bottom:3px">EXCELLENCE OPÉRATIONNELLE</div>Analyse des flux. Écoute client. Benchmark concurrentiel.</div>
      <div style="width:46px;height:74px;background:var(--pink);padding:3px;font-size:3.5px;line-height:1.35"><div class="display" style="font-size:5.5px;margin-bottom:3px">COMMUNICATION DIGITALE</div>Contribution de la marque. Stratégie des moyens. Territoire image.</div>
      <div style="width:46px;height:74px;background:var(--green);padding:3px;font-size:3.5px;line-height:1.35"><div class="display" style="font-size:5.5px;margin-bottom:3px">ORGANISATION DU SYSTÈME D'INFORMATION</div>Mise en cohérence. Sécurité. Urbanisation. Feuille de route.</div>
    </div>
    <div class="brand">Tarnobe</div>
  </section>

  <!-- 16 jour 3 -->
  <section class="slide">
    <div class="kicker" style="color:var(--green)">2/ PROCESS DÉTAILLÉ</div>
    <div class="display title" style="top:32px;font-size:19px">JOUR 3 : LES LEVIERS DE<br>LA TRANSFORMATION</div>
    <div class="display" style="position:absolute;left:18px;top:76px;display:flex;font-size:5.5px;text-align:center;line-height:1.2">
      <div style="width:66px;height:40px;background:var(--red);display:flex;align-items:center;justify-content:center;clip-path:polygon(0 0,88% 0,100% 50%,88% 100%,0 100%)">Agilité et amélioration<br>continue</div>
      <div style="width:60px;height:40px;background:var(--orange);margin-left:-6px;display:flex;align-items:center;justify-content:center;clip-path:polygon(0 0,88% 0,100% 50%,88% 100%,0 100%,12% 50%)">Mash-up (inspiration<br>sur les usages<br>d'autres)</div>
      <div style="width:66px;height:40px;background:var(--green);margin-left:-6px;display:flex;align-items:center;justify-content:center;clip-path:polygon(0 0,88% 0,100% 50%,88% 100%,0 100%,12% 50%)">Anticipation sur les<br>nouvelles technologies<br>et applications</div>
      <div style="width:60px;height:40px;background:var(--pink);margin-left:-6px;display:flex;align-items:center;justify-content:center;clip-path:polygon(0 0,88% 0,100% 50%,88% 100%,0 100%,12% 50%)">Les bonnes pratiques<br>du marché</div>
    </div>
    <div class="display" style="position:absolute;left:62px;top:124px;font-size:8.5px;color:var(--green)">PREMIÈRES HYPOTHÈSES DE TRANSFORMATION</div>
    <div class="brand">Tarnobe</div>
  </section>

  <!-- 17 jour 4 -->
  <section class="slide">
    <div class="kicker" style="color:var(--green)">2/ PROCESS DÉTAILLÉ</div>
    <div class="display title" style="top:32px;font-size:19px">JOUR 4 : TRANSFORMER LA<br>FAÇON DONT ON DOIT SE TRANSFORMER</div>
    <div style="position:absolute;left:18px;top:84px;display:flex;font-size:3.6px;font-weight:700;text-align:center;line-height:1.2">
      <div style="width:40px;height:24px;background:var(--red);display:flex;align-items:center;justify-content:center;clip-path:polygon(0 0,82% 0,100% 50%,82% 100%,0 100%)">Focus<br>impact clients</div>
      <div style="width:40px;height:24px;background:var(--orange);margin-left:-6px;display:flex;align-items:center;justify-content:center;clip-path:polygon(0 0,82% 0,100% 50%,82% 100%,0 100%,18% 50%)">Focus<br>technos</div>
      <div style="width:40px;height:24px;background:var(--green);margin-left:-6px;display:flex;align-items:center;justify-content:center;clip-path:polygon(0 0,82% 0,100% 50%,82% 100%,0 100%,18% 50%)">Focus<br>data</div>
      <div style="width:40px;height:24px;background:var(--pink);margin-left:-6px;display:flex;align-items:center;justify-content:center;clip-path:polygon(0 0,82% 0,100% 50%,82% 100%,0 100%,18% 50%)">Focus excellence<br>opérationnelle</div>
      <div style="width:40px;height:24px;background:var(--blue);margin-left:-6px;display:flex;align-items:center;justify-content:center;clip-path:polygon(0 0,82% 0,100% 50%,82% 100%,0 100%,18% 50%)">Focus<br>talents</div>
      <div style="width:40px;height:24px;background:var(--purple);margin-left:-6px;display:flex;align-items:center;justify-content:center;clip-path:polygon(0 0,82% 0,100% 50%,82% 100%,0 100%,18% 50%)">Focus réalité<br>économique</div>
      <div style="width:40px;height:24px;background:var(--orange);margin-left:-6px;display:flex;align-items:center;justify-content:center;clip-path:polygon(0 0,82% 0,100% 50%,82% 100%,0 100%,18% 50%)">Focus identité<br>&amp; usage</div>
    </div>
    <div class="display" style="position:absolute;left:16px;top:122px;font-size:8.5px">PISTES DE SOLUTIONS ÉMERGENTES DE LA PLURIDISCIPLINARITÉ</div>
    <div class="brand">Tarnobe</div>
  </section>

  <!-- 18 jour 5 -->
  <section class="slide">
    <div class="kicker" style="color:var(--green)">2/ PROCESS DÉTAILLÉ</div>
    <div class="display title" style="top:34px;font-size:22px">JOUR 5 : ON SE LANCE !</div>
    <div class="display" style="position:absolute;left:14px;top:63px;font-size:9px">PRÉSENTER NOS RECOMMANDATIONS GLOBALES</div>
    <div class="display" style="position:absolute;left:14px;top:90px;display:flex;gap:5px;align-items:center;text-align:center;font-size:4.5px;line-height:1.1">
      <div style="width:30px;height:30px;border-radius:50%;background:var(--red);border:1px solid #fff;display:flex;align-items:center;justify-content:center">Vos atouts<br>vos faiblesses</div>
      <div style="width:30px;height:30px;border-radius:50%;background:var(--orange);border:1px solid #fff;display:flex;align-items:center;justify-content:center">Vos urgences<br>stratégiques</div>
      <div style="width:30px;height:30px;border-radius:50%;background:var(--green);border:1px solid #fff;display:flex;align-items:center;justify-content:center">Les quick<br>wins</div>
      <div style="width:30px;height:30px;border-radius:50%;background:var(--pink);border:1px solid #fff;display:flex;align-items:center;justify-content:center">L'agenda<br>le budget<br>les 18 mois</div>
      <div style="width:60px;height:60px;margin-left:6px;border-radius:50%;background:var(--blue);border:2px solid #fff;display:flex;align-items:center;justify-content:center;font-size:9px">Vers une<br>nouvelle<br>ambition</div>
    </div>
    <div class="brand">Tarnobe</div>
  </section>

  <!-- 19 jour d'après -->
  <section class="slide">
    <div class="kicker" style="color:var(--green)">2/ PROCESS DÉTAILLÉ</div>
    <div class="display title" style="top:34px;font-size:22px">LE JOUR D'APRÈS</div>
    <div style="position:absolute;left:14px;top:76px;width:140px;font-size:7.5px;line-height:1.3">Capacité d'accompagnement opérationnelle sur l'ensemble des problématiques identifiées dans le sprint</div>
    <div class="figure-runner" role="img" aria-label="Coureur stylisé en facettes colorées" style="left:186px;top:20px;width:40px;height:104px"></div>
    <div class="brand">Tarnobe</div>
  </section>

  <!-- 20 section 3 -->
  <section class="slide">
    <div class="big-num" style="left:54px;color:var(--pink)">3</div>
    <div class="display section-title" style="top:62px">RÉFÉRENCES<br>DES EXPERTS</div>
    <div class="brand">Tarnobe</div>
  </section>

  <!-- 21 refs -->
  <section class="slide">
    <div class="kicker" style="color:var(--pink)">3/ RÉFÉRENCES DES EXPERTS</div>
    <div class="display title" style="top:34px;font-size:22px">RÉFÉRENCES DES EXPERTS</div>
    <table class="refs">
      <tr><td class="client">Aérolia :</td><td>De l'optimisation d'un positionnement de la marque à la redéfinition des périmètres de responsabilité des communicants</td></tr>
      <tr><td class="client">Vesta Invest :</td><td>Coaching de l'équipe datascience, thématique optimisation de l'effort commercial du réseau</td></tr>
      <tr><td class="client">Institut Nova :</td><td>Des valeurs à la création d'un manifeste identitaire et son appropriation par les collaborateurs</td></tr>
      <tr><td class="client">Clinique Saint-Lys :</td><td>De la définition d'une nouvelle politique de communication à un nouvel engagement au service des patients</td></tr>
      <tr><td class="client">Télvia :</td><td>Formations intra-entreprise sur les solutions d'architectures big data</td></tr>
      <tr><td class="client">Mutelia :</td><td>Coaching équipe data science et cartographie des axes de valorisation de données</td></tr>
      <tr><td class="client">Interpro :</td><td>Diagnostic de performance du réseau commercial en exploitant toutes les ressources de données disponibles</td></tr>
    </table>
    <div class="brand">Tarnobe</div>
  </section>

  <!-- 22 refs -->
  <section class="slide">
    <div class="kicker" style="color:var(--pink)">3/ RÉFÉRENCES DES EXPERTS</div>
    <div class="display title" style="top:34px;font-size:22px">RÉFÉRENCES DES EXPERTS</div>
    <table class="refs">
      <tr><td class="client">Qualimetre :</td><td>Enrichissement de leur offre produit (enquête de satisfaction client) pour en faire un outil de management de réseau</td></tr>
      <tr><td class="client">Cabinet Orvane :</td><td>De l'accompagnement d'une fusion (Conseilia et Stratège Partners) à la définition d'une stratégie de communication</td></tr>
      <tr><td class="client">Cadrea :</td><td>Découverte du design thinking, faciliter la prise de risque et développer la créativité de l'équipe</td></tr>
      <tr><td class="client">Fonds Public Central :</td><td>Coaching de design thinking pour proposer un soutien à une grande candidature</td></tr>
      <tr><td class="client">Batira :</td><td>Coaching de design thinking pour plus de transversalité</td></tr>
      <tr><td class="client">Batira Construction :</td><td>Travail collaboratif avec des entreprises partenaires et des métiers différents</td></tr>
      <tr><td class="client">Atelier RH :</td><td>Définition des besoins et solutions pour un outil de feedback interne à l'entreprise</td></tr>
      <tr><td class="client">Banque Meridia :</td><td>Mise en place de la nouvelle génération des centres d'appels</td></tr>
    </table>
    <div class="brand">Tarnobe</div>
  </section>

  <!-- 23 refs -->
  <section class="slide">
    <div class="kicker" style="color:var(--pink)">3/ RÉFÉRENCES DES EXPERTS</div>
    <div class="display title" style="top:34px;font-size:22px">RÉFÉRENCES DES EXPERTS</div>
    <table class="refs">
      <tr><td class="client">Datalis :</td><td>Réorganisation de l'entité produit de l'éditeur</td></tr>
      <tr><td class="client">Assistia :</td><td>Médiation sociale / optimisation du parcours métier</td></tr>
      <tr><td class="client">Réseau Plus :</td><td>Refonte des process métier de la cellule recours (dernière réponse au client avant poursuite judiciaire)</td></tr>
      <tr><td class="client">Banque Centrale Nord :</td><td>Architecture et mise en place de la plateforme d'intégration continue, mise en place de microservices</td></tr>
      <tr><td class="client">Matériaux Distribution :</td><td>Optimisation des équipes Java/JEE</td></tr>
      <tr><td class="client">Protexa :</td><td>Architecture applicative, TeachLead</td></tr>
      <tr><td class="client">Assur Bâti :</td><td>Expert Java/JEE, architecture applicative</td></tr>
    </table>
    <div class="brand">Tarnobe</div>
  </section>

  <!-- 24 closing quote -->
  <section class="slide">
    <div class="display quote" style="left:20px;top:58px;font-size:17px;line-height:1.35">« L'ENTREPRISE DIGITALISÉE, C'EST QUAND<br>ON NE PARLE PLUS DU DIGITAL ! »</div>
    <div class="brand">Tarnobe</div>
  </section>

</main>
</body>
</html>
```